Creative label for amber glass candle jar.

We are a candle company. Our products are handmade by us and natural. We are looking for something minimalistic and unique. We need a label for our candle jars (amber glass with black lid). Our current label doesn't match these requirements. We would like our products to be stocked in London shop, therefore design has to be up to a high standard. Jar specification Diameter (mm) 65 Height without cap (mm) 80. We want the new design to be different from the current one. It's just a guide for wording.
We should be able adjust the label, to change scent name.
Our scents are
*Coconut & Vanilla
*Lavender
*Bergamot
*Tuscan Orchard
*Hygge
*Eucalyptus & Peppermint
*Coffee
*Cedarwood & Juniperberry
To know more about us, visit our website www.wrenfieldcandles.com or instagram.com/wrenfieldcandles
Good luck!
Industry/Entity Type
It Company
Colors
Designer to choose colors to be used in the design.
Requirements
Must have
- * I have attached two of our logos, label design must include one of them.
- *has to mention that it's made in London
- *has to say that candle is natural/made with essential oils
- *has to have scent name and No. on it..
- Label can be vertical or horizontal, but has to be square/rectangular,.
Should not have
- Label should not be round

```html
<!DOCTYPE html>
<html lang="en">
<head>
<meta charset="utf-8">
<title>Wrenfield — No 7 Tuscan Orchard label</title>
<link href="https://fonts.googleapis.com/css2?family=Allura&family=Josefin+Sans:wght@300;400&display=swap" rel="stylesheet">
<style>
  :root {
    --backdrop: #a9a9a9;
    --label: #2b2b2b;
    --ink: #f2f2f2;
    --rule: #d9d9d9;
  }
  html, body {
    margin: 0;
    padding: 0;
    width: 1200px;
    height: 1200px;
    overflow: hidden;
    background: var(--backdrop);
  }
  .canvas {
    position: relative;
    width: 1200px;
    height: 1200px;
  }
  .label {
    position: absolute;
    left: 50px;
    top: 435px;
    width: 1100px;
    height: 330px;
    background: var(--label);
    color: var(--ink);
  }
  .brand {
    position: absolute;
    left: 50px;
    top: 0;
    height: 330px;
    width: 220px;
    display: flex;
    align-items: center;
    gap: 14px;
    font-family: "Josefin Sans", sans-serif;
    font-weight: 300;
    font-size: 26px;
    letter-spacing: 6px;
    color: var(--ink);
  }
  .brand-square {
    width: 14px;
    height: 14px;
    border: 1.5px solid var(--rule);
    flex: none;
  }
  .frame {
    position: absolute;
    left: 300px;
    top: 0;
    width: 740px;
    height: 330px;
  }
  .frame svg {
    position: absolute;
    inset: 0;
  }
  .scent-number {
    position: absolute;
    top: 42px;
    left: 0;
    width: 100%;
    text-align: center;
    font-family: "Josefin Sans", sans-serif;
    font-weight: 400;
    font-size: 34px;
    letter-spacing: 1px;
  }
  .scent-name {
    position: absolute;
    top: 96px;
    left: 0;
    width: 100%;
    text-align: center;
    font-family: "Allura", cursive;
    font-size: 96px;
    line-height: 1;
  }
  .details {
    position: absolute;
    top: 212px;
    left: 0;
    width: 100%;
    margin: 0;
    text-align: center;
    font-family: "Josefin Sans", sans-serif;
    font-weight: 300;
    font-size: 22px;
    line-height: 1.45;
    letter-spacing: 0.5px;
  }
</style>
</head>
<body>
<main class="canvas">
  <section class="label">
    <div class="brand"><span class="brand-square"></span>WRENFIELD</div>
    <div class="frame">
      <svg width="740" height="330" viewBox="0 0 740 330" aria-hidden="true">
        <g fill="none" stroke="var(--rule)" stroke-width="2">
          <polyline points="310,60 0,60 0,285 740,285 740,60 430,60"/>
        </g>
      </svg>
      <div class="scent-number">NO 7</div>
      <div class="scent-name">Tuscan Orchard</div>
      <p class="details">100% natural&nbsp; soy wax candle with essential oils<br>made in London</p>
    </div>
  </section>
</main>
</body>
</html>
```